Wealth Education Business Needs Sharp Business Card Design

We need a business card design for a recently launched investor education business called Harbor Crest.

The final design should promote security, empowerment, self improvement and financial gain. The card will ideally promote the stature of the business.

For more information and colours please visit harborcrest.com.au

Target Market(s)

Corporate executives and high net worth individuals

Industry/Entity Type

Education

Contact Information for Business Card

Name
Position
Contact Address
Phone
Mobile
Email
Website

```html
<!DOCTYPE html>
<html lang="en">
<head>
<meta charset="utf-8">
<title>Harbor Crest Business Card</title>
<link href="https://fonts.googleapis.com/css2?family=PT+Sans+Narrow:wght@400;700&display=swap" rel="stylesheet">
<style>
  :root {
    --backdrop: #e4e5e7;
    --card: #ffffff;
    --ink: #1c1c1c;
    --logo-ink: #3a3a3a;
    --green: #7dbb3a;
    --teal: #1b8a8c;
    --teal-dark: #0f6f72;
    --blue: #2fa3d8;
  }
  * { margin: 0; padding: 0; box-sizing: border-box; }
  html, body { width: 1200px; height: 1000px; overflow: hidden; }
  body {
    background: var(--backdrop);
    font-family: "PT Sans Narrow", "Arial Narrow", sans-serif;
    position: relative;
  }
  .card {
    position: absolute;
    width: 560px;
    height: 320px;
    background: var(--card);
    box-shadow: 0 6px 18px rgba(0,0,0,.12);
    overflow: hidden;
  }
  .card--back { left: 60px; top: 110px; }
  .card--front { left: 580px; top: 560px; }

  .wordmark {
    position: absolute;
    display: flex;
    align-items: center;
    gap: 12px;
    color: var(--logo-ink);
    font-weight: 400;
    letter-spacing: 5px;
    text-transform: uppercase;
    white-space: nowrap;
  }
  .wordmark__dot {
    width: 26px; height: 26px;
    border-radius: 50%;
    background: var(--teal);
  }
  .card--back .wordmark {
    font-size: 30px;
    left: 50%; top: 50%;
    transform: translate(-50%, -50%);
  }
  .card--front .wordmark {
    font-size: 20px;
    left: 250px; top: 12px;
  }
  .card--front .wordmark__dot { width: 18px; height: 18px; }

  .top-band { position: absolute; left: 0; top: 46px; width: 100%; }
  .top-band__green { height: 5px; background: var(--green); }
  .top-band__teal { height: 7px; background: var(--teal); }
  .top-band__fill {
    height: 78px;
    background: linear-gradient(180deg, var(--teal) 0%, var(--blue) 35%, rgba(47,163,216,.35) 75%, rgba(255,255,255,0) 100%);
  }

  .person { position: absolute; left: 30px; top: 158px; }
  .person__name {
    font-size: 42px;
    color: var(--ink);
    text-transform: uppercase;
    line-height: 1;
    letter-spacing: -0.5px;
  }
  .person__rule { margin-top: 8px; width: 240px; }
  .person__rule span { display: block; }
  .person__rule .r-green { height: 3px; background: var(--green); }
  .person__rule .r-teal { height: 6px; background: var(--teal); }
  .person__rule .r-blue { height: 4px; background: var(--blue); }
  .person__title {
    margin-top: 12px;
    font-size: 17px;
    color: var(--green);
    text-transform: uppercase;
  }

  .contacts {
    position: absolute;
    left: 330px; top: 160px;
    list-style: none;
    font-size: 15px;
    color: var(--ink);
  }
  .contacts li {
    display: flex;
    align-items: center;
    gap: 8px;
    height: 24px;
  }
  .contacts svg { width: 16px; height: 16px; flex: none; fill: var(--green); }
</style>
</head>
<body>

<section class="card card--back">
  <div class="wordmark"><span>Harbor</span><span class="wordmark__dot"></span><span>Crest</span></div>
</section>

<section class="card card--front">
  <div class="wordmark"><span>Harbor</span><span class="wordmark__dot"></span><span>Crest</span></div>

  <div class="top-band">
    <div class="top-band__green"></div>
    <div class="top-band__teal"></div>
    <div class="top-band__fill" role="img" aria-label="Decorative band of hanging teal, blue and green rounded bars"></div>
  </div>

  <div class="person">
    <h1 class="person__name">Daniel Reyes</h1>
    <div class="person__rule">
      <span class="r-green"></span><span class="r-teal"></span><span class="r-blue"></span>
    </div>
    <p class="person__title">Business Consultant</p>
  </div>

  <ul class="contacts">
    <li>
      <svg viewBox="0 0 16 16" aria-hidden="true"><rect x="1" y="6" width="14" height="9" rx="2"/><path d="M2 5c2-3 10-3 12 0l-2 1H4z"/></svg>
      (555) 210-4830
    </li>
    <li>
      <svg viewBox="0 0 16 16" aria-hidden="true"><path d="M4 1h3l1 4-2 1c1 2 2 3 4 4l1-2 4 1v3c0 1-1 2-2 2C7 14 2 9 2 3c0-1 1-2 2-2z"/></svg>
      (555) 318-9062
    </li>
    <li>
      <svg viewBox="0 0 16 16" aria-hidden="true"><path d="M1 3h14v10H1z M1 3l7 6 7-6" stroke="#fff" stroke-width="1"/></svg>
      dreyes@harborcrest.com
    </li>
    <li>
      <svg viewBox="0 0 16 16" aria-hidden="true"><circle cx="3" cy="13" r="2"/><path d="M1 7a8 8 0 0 1 8 8h-2a6 6 0 0 0-6-6z"/><path d="M1 2a13 13 0 0 1 13 13h-2A11 11 0 0 0 1 4z"/></svg>
      www.harborcrest.com
    </li>
    <li>
      <svg viewBox="0 0 16 16" aria-hidden="true"><path d="M8 1a5 5 0 0 1 5 5c0 4-5 9-5 9S3 10 3 6a5 5 0 0 1 5-5zm0 3a2 2 0 1 0 0 4 2 2 0 0 0 0-4z"/></svg>
      48 Quay Rd, Bayview WI 54021
    </li>
  </ul>
</section>

</body>
</html>
```